Larkfield Interiors
Stationary, Letterhead & Business Card
Larkfield Interiors -
Creative Brief
Professional
Dennis Coyle
Project Manager
478 Oakmont Avenue N.W. Millbrook, OR 97215
dennis@larkfield-interiors-studio.com
The information is fake, once the winning design is selected I will forward the correct contact information to the designer.

```html
<!DOCTYPE html>
<html lang="en">
<head>
<meta charset="utf-8">
<title>Larkfield Interiors – Stationery</title>
<link href="https://fonts.googleapis.com/css2?family=Open+Sans:wght@400;600;700&display=swap" rel="stylesheet">
<style>
  :root{
    --stage:#3a3a3a;
    --paper:#ffffff;
    --orange:#f39a1e;
    --orange-light:#fbc25a;
    --orange-deep:#e07a10;
    --ink:#444444;
    --ink-soft:#7a7a7a;
    --card-grey:#e4e4e4;
    --card-grey-dark:#c9c9c9;
    --name-blue:#4a5a6e;
    --signature-fill:#ececec;
  }
  *{margin:0;padding:0;box-sizing:border-box}
  html,body{width:1200px;height:874px;overflow:hidden}
  body{background:var(--stage);font-family:"Open Sans",Arial,sans-serif;color:var(--ink);position:relative}
  .sheet{position:absolute;background:var(--paper);overflow:hidden}
  .brand{position:absolute;display:flex;align-items:center;gap:8px}
  .brand__mark{background:var(--orange);flex:none}
  .brand__name{font-family:"Open Sans",Arial,sans-serif;font-weight:700;color:var(--orange);line-height:1;letter-spacing:.04em;text-transform:uppercase}
  .swoosh{position:absolute;left:0;bottom:0;width:100%}

  /* Letterhead */
  .letterhead{left:102px;top:92px;width:511px;height:723px}
  .letterhead .brand{left:30px;top:28px}
  .letterhead .brand__mark{width:30px;height:30px}
  .letterhead .brand__name{font-size:22px}
  .letterhead__contact{position:absolute;left:30px;top:86px;font-size:6.4px;color:var(--ink-soft);white-space:nowrap}
  .letterhead__body{position:absolute;left:30px;top:132px;width:452px;font-size:9.6px;line-height:1.75;color:var(--ink)}
  .letterhead__body p{margin-bottom:12px}
  .letterhead__sign{position:absolute;left:30px;top:572px;font-size:9px}
  .letterhead__signature{margin-top:6px;width:60px;height:26px;background:var(--signature-fill)}

  /* Business cards */
  .card{top:92px;height:166px}
  .card--info{left:638px;width:274px;background:linear-gradient(180deg,var(--card-grey) 0%,var(--card-grey-dark) 100%)}
  .card--info .brand{left:12px;top:12px;gap:5px}
  .card--info .brand__mark{width:14px;height:14px}
  .card--info .brand__name{font-size:10px}
  .card__person{position:absolute;left:0;right:0;top:56px;text-align:center}
  .card__name{font-size:13px;font-weight:600;color:var(--name-blue)}
  .card__title{font-size:6.5px;color:var(--ink-soft);margin-top:1px}
  .card__contact{margin-top:10px;font-size:5.8px;line-height:1.6;color:var(--ink-soft)}
  .card--brand{left:924px;width:240px;background:linear-gradient(135deg,#ededed 0%,var(--card-grey-dark) 100%)}
  .card--brand .brand{left:0;right:0;top:0;bottom:0;justify-content:center;gap:10px}
  .card--brand .brand__mark{width:26px;height:26px}
  .card--brand .brand__name{font-size:18px}

  /* Envelope */
  .envelope-back{left:638px;top:389px;width:528px;height:219px}
  .envelope-back .brand{left:18px;top:18px;gap:6px}
  .envelope-back .brand__mark{width:18px;height:18px}
  .envelope-back .brand__name{font-size:13px}
  .envelope-back__band{position:absolute;left:0;top:60px;width:100%;height:90px}
  .envelope-front{left:638px;top:633px;width:528px;height:182px}
</style>
</head>
<body>

<section class="sheet letterhead" aria-label="Letterhead">
  <div class="brand"><span class="brand__mark"></span><span class="brand__name">Larkfield Interiors</span></div>
  <p class="letterhead__contact">478 Oakmont Avenue N.W. Millbrook, OR 97215 · Tel: 507 555 0142 · dennis@larkfield-interiors-studio.com · www.larkfield-interiors-studio.com</p>
  <div class="letterhead__body">
    <p>Thank you for considering us for your upcoming project. Our studio plans every room with care, from the first sketch to the final fitting, so that each space feels calm, practical and welcoming, and works well for the people who use it every day.</p>
    <p>We begin by listening to how you live and work, then shape a plan around light, colour and movement. Furniture, fabrics and finishes are chosen to suit your budget and your schedule, and every choice is shown to you before it is ordered. Our team manages suppliers and trades on site, keeps you informed at each stage and hands over a finished room that is ready to use on the agreed date. Samples of paint, timber and textiles are brought to your home so you can see them in your own light, and small changes are welcome at any point.</p>
    <p>Once the plan is agreed, we prepare clear drawings and a written schedule so that every trade knows what to do and when. Where walls or floors need work, we arrange it, check it and sign it off before anything new is placed in the room. Deliveries are booked around your week, protected on arrival and fitted by people we have worked with for years. At the end we walk through each space with you, note anything that needs a final touch and return to finish it promptly.</p>
    <p>Please contact me with any questions about the proposal or the timeline. I look forward to working with you.</p>
  </div>
  <div class="letterhead__sign">
    <p>Project Manager</p>
    <div class="letterhead__signature" role="img" aria-label="Handwritten signature"></div>
  </div>
  <svg class="swoosh" viewBox="0 0 511 110" height="110" preserveAspectRatio="none" aria-hidden="true">
    <defs>
      <linearGradient id="lhGrad" x1="0" x2="1">
        <stop offset="0" stop-color="#fbc25a"/><stop offset="1" stop-color="#f39a1e"/>
      </linearGradient>
    </defs>
    <path d="M0 70 C150 95 330 60 511 10 L511 110 L0 110 Z" fill="url(#lhGrad)"/>
    <path d="M0 88 C170 108 340 80 511 40 L511 110 L0 110 Z" fill="#e07a10"/>
    <path d="M0 60 C150 88 330 52 511 0" fill="none" stroke="#f39a1e" stroke-width="1.5"/>
  </svg>
</section>

<section class="sheet card card--info" aria-label="Business card, contact side">
  <div class="brand"><span class="brand__mark"></span><span class="brand__name">Larkfield Interiors</span></div>
  <div class="card__person">
    <p class="card__name">Dennis Coyle</p>
    <p class="card__title">Project Manager</p>
    <p class="card__contact">478 Oakmont Avenue N.W. Millbrook, OR 97215<br>Tel: 507 555 0142<br>dennis@larkfield-interiors-studio.com</p>
  </div>
  <svg class="swoosh" viewBox="0 0 274 40" height="40" preserveAspectRatio="none" aria-hidden="true">
    <path d="M0 28 C90 40 190 24 274 4 L274 40 L0 40 Z" fill="#f39a1e"/>
    <path d="M0 35 C100 44 200 30 274 18 L274 40 L0 40 Z" fill="#e07a10"/>
  </svg>
</section>

<section class="sheet card card--brand" aria-label="Business card, brand side">
  <div class="brand"><span class="brand__mark"></span><span class="brand__name">Larkfield</span></div>
</section>

<section class="sheet envelope-back" aria-label="Envelope back">
  <div class="brand"><span class="brand__mark"></span><span class="brand__name">Larkfield Interiors</span></div>
  <svg class="envelope-back__band" viewBox="0 0 528 90" preserveAspectRatio="none" aria-hidden="true">
    <defs>
      <linearGradient id="envGrad" x1="0" x2="1">
        <stop offset="0" stop-color="#fbc25a"/><stop offset="1" stop-color="#f39a1e"/>
      </linearGradient>
    </defs>
    <path d="M0 40 C180 60 360 30 528 0 L528 50 C360 80 180 90 0 70 Z" fill="url(#envGrad)"/>
    <path d="M0 70 C180 90 360 80 528 50 L528 62 C360 90 180 96 0 80 Z" fill="#e07a10"/>
  </svg>
</section>

<section class="sheet envelope-front" aria-label="Envelope front">
  <svg class="swoosh" viewBox="0 0 528 60" height="60" preserveAspectRatio="none" aria-hidden="true">
    <path d="M0 40 C180 60 360 36 528 4 L528 60 L0 60 Z" fill="#fbc25a"/>
    <path d="M0 50 C190 66 370 48 528 24 L528 60 L0 60 Z" fill="#f39a1e"/>
  </svg>
</section>

</body>
</html>
```